International Clinical Software Company needs a new business card design

We are looking for a new business card design for our company that has recently expanded into the UK market, making us a multinational company.
After having rebranded our website and produced a new style guide, we are looking for a business card that is creative and attention grabbing, while being consistent with the style and colour scheme used on the new website, www.brookvale.example
We produce care management technology for the aged care market, but the main aspect we aim to communicate is the human element of our software, and the way it assists in providing better care for aged people, and stronger relationships between aged people and the staff that care for them.
Our current business card is a dark green with gold text, which makes the text quite difficult to read, not very aesthetically appealing and the colour scheme looks quite dated.
We would like something fresh and modern, that can still be colourful but doesn't use large blocks of dark colour, and uses the colours within our logo.
Something tying in with the leaves that are used in our logo could work quite nicely, along with the Autumn/Fall colours of soft greens, yellows and reds (also in our existing logo). However also happy to look at fresh, completely out of the box ideas we may not have yet considered.
Target Market(s)
The people that receive this business card work in the aged card or health industry and are either corporate/management level staff or clinical (Registered Nurses, care workers etc.)
Industry/Entity Type
Health Product
Contact Information for Business Card
Company Name - BrookvaleTech
Company locations: United Kingdom, Australia, New Zealand
Staff Details:
Staff name: Dermot Quill
Staff job title: Executive Chairman
Staff email: d.quill@brookvale.example
Office phone number: 01632 960418
Font styles to use
Other font styles liked:
- Calibri
Requirements
Must have
- Must include the BrookvaleTech brand name in it's current font
- Must include logo (3 leaves in gold circle)
- Must include Business Card Details
Nice to have
- Elements of gold
- White space
- Something autumn themed but not too cliched
Should not have
- No blue - used by a major competitor and we would like to differentiate from them
- Large blocks of dark green colour (the green that appears in our leaves on the logo on our current business card is the background colour and it is far too dark)

```html
<!DOCTYPE html>
<html lang="en">
<head>
<meta charset="utf-8">
<title>BrookvaleTech Business Card</title>
<link rel="stylesheet" href="https://fonts.googleapis.com/css2?family=Arimo:wght@400;700&display=swap">
<style>
  :root {
    --page-bg: #f4f4f4;
    --card-bg: #ffffff;
    --gold: #b29f6e;
    --ink: #1a1a1a;
    --panel-dark: #1b1b1b;
    --light-text: #ffffff;
  }
  * { box-sizing: border-box; margin: 0; padding: 0; }
  html, body {
    width: 1200px;
    height: 528px;
    overflow: hidden;
    background: var(--page-bg);
    font-family: "Arimo", Arial, sans-serif;
  }
  .card {
    position: absolute;
    top: 90px;
    width: 543px;
    height: 310px;
    background: var(--card-bg);
    overflow: hidden;
  }
  .card-front { left: 37px; }
  .card-back { left: 620px; }

  .swoosh { position: absolute; inset: 0; width: 543px; height: 310px; }

  .brand-lockup {
    position: absolute;
    display: flex;
    align-items: center;
    color: var(--gold);
    font-weight: 400;
    white-space: nowrap;
  }
  .brand-mark {
    border: 3px solid var(--gold);
    border-radius: 50%;
    flex: none;
  }
  .card-front .brand-lockup { left: 10px; top: 25px; gap: 12px; font-size: 30px; }
  .card-front .brand-mark { width: 110px; height: 110px; }
  .card-back .brand-lockup { left: 56px; top: 77px; gap: 20px; font-size: 46px; }
  .card-back .brand-mark { width: 156px; height: 156px; }

  .person {
    position: absolute;
    left: 30px;
    top: 158px;
    width: 192px;
    text-align: center;
    color: var(--ink);
  }
  .person-name { font-size: 25px; font-weight: 700; line-height: 1.2; }
  .person-title { font-size: 15px; margin-top: 6px; }

  .contact {
    position: absolute;
    right: 20px;
    top: 152px;
    text-align: right;
    color: var(--light-text);
    font-size: 15px;
    line-height: 20px;
  }
  .contact-company { color: var(--gold); font-size: 27px; line-height: 32px; margin-bottom: 8px; }
  .contact-line { display: flex; justify-content: flex-end; align-items: center; gap: 10px; margin-top: 10px; }
  .contact-line svg { width: 18px; height: 18px; flex: none; }
</style>
</head>
<body>

<section class="card card-front">
  <svg class="swoosh" viewBox="0 0 543 310" aria-hidden="true">
    <path fill="var(--gold)" d="M0 310 C200 298 262 196 330 118 C390 52 470 48 543 50 L543 64 C470 62 394 72 336 128 C266 206 206 304 18 310 Z"/>
    <path fill="var(--panel-dark)" d="M30 310 C214 302 272 210 340 134 C398 78 472 68 543 70 L543 310 Z"/>
  </svg>

  <div class="brand-lockup">
    <span class="brand-mark"></span>
    <span class="brand-name">BrookvaleTech</span>
  </div>

  <div class="person">
    <div class="person-name">Dermot Quill</div>
    <div class="person-title">Executive Chairman</div>
  </div>

  <div class="contact">
    <div class="contact-company">BrookvaleTech</div>
    <div>United Kingdom, Australia,</div>
    <div>New Zealand</div>
    <div class="contact-line">
      <span>d.quill@brookvale.example</span>
      <svg viewBox="0 0 18 18" aria-hidden="true">
        <rect x="1" y="4" width="16" height="11" fill="var(--gold)"/>
        <path d="M1 4 L9 10 L17 4" fill="none" stroke="var(--panel-dark)" stroke-width="1.2"/>
      </svg>
    </div>
    <div class="contact-line">
      <span>www.brookvale.example</span>
      <svg viewBox="0 0 18 18" aria-hidden="true">
        <circle cx="9" cy="9" r="8" fill="var(--gold)"/>
        <ellipse cx="9" cy="9" rx="3.5" ry="8" fill="none" stroke="var(--panel-dark)" stroke-width="1"/>
        <path d="M1 9 H17" stroke="var(--panel-dark)" stroke-width="1"/>
      </svg>
    </div>
  </div>
</section>

<section class="card card-back">
  <div class="brand-lockup">
    <span class="brand-mark"></span>
    <span class="brand-name">BrookvaleTech</span>
  </div>
</section>

</body>
</html>
```